Need eyecatching label for new caramel sauce in jars.

We're an award-winning chocolate company expanding into jarred caramel and chocolate sauces. We need labels that are eye-catching but elegant, include our logo, nutritional panel and bar code. You will be designing a label for our new Jamaican Rum caramel sauce and we will use the basic layout for other flavors to come.

Colors

Designer to choose colors to be used in the design.

Requirements
Must have
• Logo, nutritional panel, UPC bar code, flavor (Jamacian rum caramel sauce)
Nice to have
• This design is for a consumer product, so it must look enticing and delicious from the shelf. I'm open to black background, custom illustrations, almost anything that conveys both deliciousness and high quality. Don't be afraid to imagine foil, UV or die cuts on the label, either. They'll be printed high quality. I would look to some of the cool wine or liquor bottles for inspiration.
Should not have
• Please do not include any dripping chocolate. That's too generic for our market. They already get that we're a chocolate company.

```html
<!DOCTYPE html>
<html lang="en">
<head>
<meta charset="utf-8">
<title>Jamaican Rum Caramel – Jar Label</title>
<link rel="stylesheet" href="https://fonts.googleapis.com/css2?family=Cinzel:wght@500&family=Rye&family=Great+Vibes&display=swap">
<style>
  :root {
    --page-bg: #f4f4f7;
    --label-black: #0d0d0d;
    --label-edge: #1e1e1e;
    --gold: #e2b84f;
    --gold-light: #f6d77e;
    --gold-deep: #a8771f;
    --cream: #f7f2e8;
  }
  * { margin: 0; padding: 0; box-sizing: border-box; }
  html, body {
    width: 1200px;
    height: 1200px;
    overflow: hidden;
    background: var(--page-bg);
  }
  .canvas {
    position: relative;
    width: 1200px;
    height: 1200px;
  }
  .label {
    position: absolute;
    left: 50px;
    top: 146px;
    width: 1100px;
    height: 908px;
    background: linear-gradient(90deg, var(--label-edge) 0%, var(--label-black) 15%, var(--label-black) 85%, var(--label-edge) 100%);
  }
  .frame-art {
    position: absolute;
    inset: 0;
    width: 1100px;
    height: 908px;
  }
  .brand {
    position: absolute;
    left: 0;
    right: 0;
    top: 83px;
    text-align: center;
    font-family: "Cinzel", serif;
    font-weight: 500;
    color: var(--gold);
  }
  .brand__mark {
    display: block;
    width: 156px;
    height: 156px;
    margin: 0 auto;
    border-radius: 50%;
    background: var(--gold);
  }
  .brand__name {
    display: block;
    margin-top: 44px;
    font-size: 42px;
    line-height: 1;
    letter-spacing: 1px;
  }
  .brand__sub {
    display: block;
    margin-top: 10px;
    font-size: 17px;
    line-height: 1;
    letter-spacing: 5px;
  }
  .divider {
    position: absolute;
    left: 284px;
    top: 391px;
    width: 549px;
    height: 2px;
    background: linear-gradient(90deg, rgba(168,119,31,0) 0%, var(--gold-deep) 20%, var(--gold-deep) 80%, rgba(168,119,31,0) 100%);
  }
  .divider::after {
    content: "";
    position: absolute;
    left: 50%;
    top: -4px;
    width: 9px;
    height: 9px;
    background: var(--gold);
    transform: translateX(-50%) rotate(45deg);
  }
  .flavor {
    position: absolute;
    left: 0;
    right: 0;
    top: 408px;
    text-align: center;
    font-family: "Rye", serif;
    font-weight: 400;
    font-size: 88px;
    line-height: 1;
    color: var(--gold-light);
    background: linear-gradient(180deg, var(--gold-light) 0%, var(--gold) 55%, var(--gold-deep) 100%);
    -webkit-background-clip: text;
    background-clip: text;
    -webkit-text-fill-color: transparent;
  }
  .product {
    position: absolute;
    left: 0;
    right: 0;
    top: 500px;
    text-align: center;
    font-family: "Great Vibes", cursive;
    font-size: 128px;
    line-height: 1;
    color: var(--cream);
  }
  .maker {
    position: absolute;
    left: 0;
    right: 0;
    top: 730px;
    text-align: center;
    font-family: "Cinzel", serif;
    font-weight: 500;
    font-size: 25px;
    letter-spacing: 1px;
    color: var(--gold);
  }
</style>
</head>
<body>
  <main class="canvas">
    <section class="label">
      <svg class="frame-art" viewBox="0 0 1100 908">
        <defs>
          <linearGradient id="leaf-gold" x1="0" y1="0" x2="1" y2="1">
            <stop offset="0" stop-color="#f6d77e"/>
            <stop offset="0.55" stop-color="#d6a53c"/>
            <stop offset="1" stop-color="#8a5f17"/>
          </linearGradient>
          <g id="corner">
            <g fill="none" stroke="#e2b84f">
              <path d="M53 365 V70 H345" stroke-width="2"/>
              <path d="M62 355 V79 H335" stroke-width="1"/>
            </g>
            <path d="M72 88 H330 Q320 120 290 128 H150 Q128 132 124 155 V330 Q110 345 96 352 Q72 300 72 250 Z" fill="url(#leaf-gold)" opacity="0.9"/>
          </g>
        </defs>

        <g role="img" aria-label="Gold acanthus leaf flourish, top left corner">
          <use href="#corner"/>
        </g>
        <g role="img" aria-label="Gold acanthus leaf flourish, top right corner" transform="translate(1100,0) scale(-1,1)">
          <use href="#corner"/>
        </g>
        <g role="img" aria-label="Gold acanthus leaf flourish, bottom left corner" transform="translate(0,908) scale(1,-1)">
          <use href="#corner"/>
        </g>
        <g role="img" aria-label="Gold acanthus leaf flourish, bottom right corner" transform="translate(1100,908) scale(-1,-1)">
          <use href="#corner"/>
        </g>

        <rect role="img" aria-label="Small cream scroll ornament" x="68" y="414" width="26" height="62" rx="13" fill="#f7f2e8" opacity="0.85"/>
        <rect role="img" aria-label="Small cream scroll ornament" x="1006" y="414" width="26" height="62" rx="13" fill="#f7f2e8" opacity="0.85"/>

        <rect role="img" aria-label="Cream filigree scroll leading into the product name" x="170" y="570" width="168" height="16" rx="8" fill="#f7f2e8" opacity="0.85"/>
        <rect role="img" aria-label="Cream filigree scroll trailing the product name" x="836" y="570" width="168" height="16" rx="8" fill="#f7f2e8" opacity="0.85"/>
      </svg>

      <header class="brand">
        <span class="brand__mark"></span>
        <span class="brand__name">HARBOR ISLE</span>
        <span class="brand__sub">CHOCOLATE CO.</span>
      </header>

      <div class="divider"></div>

      <h1 class="flavor">JAMAICAN RUM</h1>
      <p class="product">Caramel</p>

      <p class="maker">MARLEN VOSSBERG</p>
    </section>
  </main>
</body>
</html>
```